Kids Bamboo sun protection clothing

We need a flyer to promote our bamboo sun protection range to parents of kids with sensitive due to illness or skin conditions.
Our clothing is made from bamboo that has been specially knitted for high sun protection but does not use chemicals. The clothing is for everyday wear, to the playground, going for walks, after a swim. Special features such as hoods, high necklines, long sleeves and thumb loops create more coverage but it is not a lycra rash vest. You can see the product at www.lumora-wear.com. We would like this flyer (or postcard) to show parents with children who are sensitive tot he sun that there is an option. Their kids might have albinism, Cancer or severe burns, might be sensitive to the sun or have Eczema. These clothes are natural fabric with styling to help look after their skin in the sun. We would like a soft caring approach.

Target Market(s)

Mums of children who have sensitive skin due to burns, cancer, Eczema or UV sensitivity.

Industry/Entity Type

Health

Font styles to use
Sans Serif

Requirements
Must have
• Point out how it can protect the skin with fabric and design features.
• Be eye catching so if it is in a waiting room at the doctors people will go over to pick it up. Be a soft approach that does not concentrate on the illness.
• Website details
Nice to have
• mention that we also do women's wear
• Please use any images off the website

```html
<!DOCTYPE html>
<html lang="en">
<head>
<meta charset="utf-8">
<title>Lumora Kids Clothing – Postcard</title>
<link href="https://fonts.googleapis.com/css2?family=Lato:ital,wght@0,300;0,400;0,700;1,400;1,700&display=swap" rel="stylesheet">
<style>
  :root{
    --orange:#f7a42b;
    --dark:#333333;
    --ink:#1c1c1c;
    --white:#ffffff;
    --stamp:#c4c4c4;
    --canvas:#dcdcdc;
    --logo-grey:#4a4a4a;
  }
  *{box-sizing:border-box;margin:0;padding:0}
  html,body{width:1200px;height:1200px;overflow:hidden}
  body{background:var(--canvas);font-family:"Lato",sans-serif;color:var(--ink);position:relative}
  .card{position:absolute;left:210px;width:780px;height:500px;overflow:hidden;box-shadow:0 10px 24px rgba(0,0,0,.18);background:var(--white)}
  .card--front{top:60px}
  .card--back{top:640px}
  .card__shapes{position:absolute;inset:0;width:780px;height:500px}
  .abs{position:absolute}

  /* front */
  .title{left:400px;top:52px;line-height:1;font-weight:400}
  .title__brand{display:block;font-size:46px;color:var(--ink);letter-spacing:1px}
  .title__product{display:block;font-size:62px;color:var(--orange);letter-spacing:2px;margin-top:4px}
  .intro{left:402px;top:182px;width:350px;font-size:12.5px;line-height:1.35}
  .care-box{left:522px;top:302px;width:232px;font-size:11px;line-height:1.35}
  .care-box__lead{font-style:italic;font-weight:700;margin-bottom:3px}
  .care-box ul{list-style:none}
  .care-box li{padding-left:11px;position:relative}
  .care-box li::before{content:"";position:absolute;left:0;top:5px;width:6px;height:6px;border-radius:50%;background:var(--ink)}
  .care-box__close{font-style:italic;font-weight:700;margin-top:4px}
  .find-us{color:var(--white);font-size:14px;font-weight:700;letter-spacing:.3px;white-space:nowrap}
  .find-us--front{left:506px;top:456px}
  .brand-mark{font-weight:300;color:var(--logo-grey);letter-spacing:3px;line-height:1;white-space:nowrap}
  .brand-mark--front{left:110px;top:402px;font-size:40px}
  .brand-mark--back{left:38px;top:50px;font-size:46px}

  /* back */
  .range-note{left:40px;top:212px;width:280px;color:var(--white);font-size:13.5px;line-height:1.3}
  .story{left:40px;top:295px;width:360px;font-size:10.5px;line-height:1.35}
  .story b{font-weight:700}
  .features{left:54px;top:359px;width:250px;font-size:10.5px;line-height:1.35;display:flex;gap:18px}
  .features__label{color:var(--orange);font-weight:700;display:block}
  .features ul{list-style:none}
  .features__col2{padding-top:8px}
  .features li{padding-left:10px;position:relative}
  .features li::before{content:"";position:absolute;left:0;top:5px;width:5px;height:5px;border-radius:50%;background:var(--ink)}
  .contact{left:40px;top:412px;font-size:11px;line-height:1.3;white-space:nowrap}
  .find-us--back{left:40px;top:469px}
</style>
</head>
<body>

<section class="card card--front" aria-label="Postcard front">
  <svg class="card__shapes" viewBox="0 0 780 500">
    <defs>
      <linearGradient id="bgFront" x1="0" y1="0" x2="1" y2="1">
        <stop offset="0" stop-color="#fafafa"/><stop offset="1" stop-color="#e4e4e4"/>
      </linearGradient>
      <linearGradient id="photoStripe" x1="0" y1="0" x2="0" y2="1">
        <stop offset="0" stop-color="#e9e7e3"/><stop offset="1" stop-color="#9aa0b2"/>
      </linearGradient>
      <linearGradient id="photoBlue" x1="0" y1="0" x2="0" y2="1">
        <stop offset="0" stop-color="#ecebe8"/><stop offset="1" stop-color="#a9c1d8"/>
      </linearGradient>
      <linearGradient id="photoPair" x1="0" y1="0" x2="1" y2="0">
        <stop offset="0" stop-color="#e7bfd8"/><stop offset="1" stop-color="#2c3552"/>
      </linearGradient>
    </defs>
    <rect width="780" height="500" fill="url(#bgFront)"/>
    <polygon points="0,0 175,0 60,500 0,500" fill="var(--dark)"/>
    <polygon points="175,0 205,0 90,500 60,500" fill="var(--orange)"/>
    <rect x="150" y="258" width="630" height="8" fill="var(--dark)"/>
    <rect x="150" y="266" width="630" height="8" fill="var(--orange)"/>
    <polygon points="320,500 355,440 780,440 780,490 330,500" fill="var(--orange)"/>
    <polygon points="300,500 330,460 345,460 320,500" fill="var(--dark)"/>
    <rect x="0" y="490" width="780" height="10" fill="var(--dark)"/>
    <line x1="110" y1="394" x2="270" y2="394" stroke="var(--orange)" stroke-width="2"/>

    <polygon points="90,125 142.5,34 247.5,34 300,125 247.5,216 142.5,216" fill="var(--white)" stroke="var(--orange)" stroke-width="4"/>
    <polygon points="103,125 149,45 241,45 287,125 241,205 149,205" fill="url(#photoStripe)" role="img" aria-label="Photo: boy in a striped long-sleeve bamboo top and shorts"/>
    <polygon points="80,320 115,259 185,259 220,320 185,381 115,381" fill="var(--white)" stroke="var(--orange)" stroke-width="4"/>
    <polygon points="92,320 121,270 179,270 208,320 179,370 121,370" fill="url(#photoBlue)" role="img" aria-label="Photo: girl in a light blue hooded bamboo top"/>
    <rect x="340" y="290" width="150" height="200" fill="url(#photoPair)" opacity=".85" role="img" aria-label="Photo: girl in a pink dress and boy in a striped hooded top"/>

    <rect x="510" y="292" width="254" height="124" rx="16" fill="var(--white)" stroke="var(--orange)" stroke-width="2"/>
  </svg>

  <h1 class="abs title"><span class="title__brand">LUMORA KIDS</span><span class="title__product">CLOTHING</span></h1>
  <p class="abs intro">Our children's skin is so soft and delicate. Some little ones need extra protection from the sun in a way that cares for their delicate skin.</p>
  <div class="abs care-box">
    <p class="care-box__lead">If your little one -</p>
    <ul>
      <li>Has sensitive skin due to medication</li>
      <li>Has a burn or scar that is not sun friendly</li>
      <li>Is sensitive to uncomfortable clothes</li>
      <li>Or is UV sensitive</li>
    </ul>
    <p class="care-box__close">Then we might be able to help!</p>
  </div>
  <p class="abs brand-mark brand-mark--front">LUMORA</p>
  <p class="abs find-us find-us--front">FIND US A WWW.LUMORA-WEAR.COM</p>
</section>

<section class="card card--back" aria-label="Postcard back">
  <svg class="card__shapes" viewBox="0 0 780 500">
    <defs>
      <linearGradient id="bgBack" x1="0" y1="0" x2="1" y2="1">
        <stop offset="0" stop-color="#e2e2e2"/><stop offset="1" stop-color="#f7f7f7"/>
      </linearGradient>
      <linearGradient id="photoTee" x1="0" y1="0" x2="0" y2="1">
        <stop offset="0" stop-color="#efeeeb"/><stop offset="1" stop-color="#2f3b5c"/>
      </linearGradient>
      <linearGradient id="photoPink" x1="0" y1="0" x2="0" y2="1">
        <stop offset="0" stop-color="#f0ece9"/><stop offset="1" stop-color="#e4aed2"/>
      </linearGradient>
    </defs>
    <rect width="780" height="500" fill="var(--white)"/>
    <polygon points="0,0 300,0 470,440 330,500 0,500" fill="url(#bgBack)"/>
    <polygon points="300,0 420,0 420,440 470,440" fill="var(--orange)"/>
    <polygon points="290,0 300,0 470,440 460,440" fill="var(--dark)"/>
    <polygon points="330,445 780,440 780,470 340,475" fill="var(--orange)"/>
    <polygon points="0,455 345,455 325,500 0,500" fill="var(--dark)"/>
    <line x1="38" y1="40" x2="240" y2="40" stroke="var(--orange)" stroke-width="2"/>

    <polygon points="20,202 340,192 370,262 20,282" fill="var(--dark)"/>
    <polyline points="20,196 340,186" stroke="var(--orange)" stroke-width="4" fill="none"/>
    <polyline points="20,288 370,268" stroke="var(--orange)" stroke-width="4" fill="none"/>

    <polygon points="370,175 410,106 490,106 530,175 490,244 410,244" fill="var(--white)" stroke="var(--orange)" stroke-width="4"/>
    <polygon points="382,175 416,116 484,116 518,175 484,234 416,234" fill="url(#photoTee)" role="img" aria-label="Photo: boy in a striped tee and navy shorts"/>
    <polygon points="460,345 490,293 550,293 580,345 550,397 490,397" fill="var(--white)" stroke="var(--orange)" stroke-width="4"/>
    <polygon points="470,345 495,302 545,302 570,345 545,388 495,388" fill="url(#photoPink)" role="img" aria-label="Photo: girl in a pink hooded bamboo top"/>

    <rect x="44" y="350" width="262" height="52" rx="14" fill="var(--white)" stroke="var(--orange)" stroke-width="2"/>
    <rect x="690" y="38" width="62" height="62" fill="var(--stamp)"/>
  </svg>

  <p class="abs brand-mark brand-mark--back">LUMORA</p>
  <p class="abs range-note">Our Little Lumora range is 100% Australian made bamboo jersey made especially for everyday sun protection</p>
  <p class="abs story">Life is for living, bring back fresh air and flowers in clothes from Lumora-wear.com. <b>Tested by Solace Labs to UPF 50+ protection, we have your head, arms, legs and hands covered for everyday life outside.</b></p>
  <div class="abs features">
    <div>
      <span class="features__label">Features:</span>
      <ul><li>High necklines</li><li>Long sleeves</li></ul>
    </div>
    <ul class="features__col2"><li>Thumb loops for hand cover</li><li>Breathable fabrics</li></ul>
  </div>
  <p class="abs contact">See more at www.lumora-wear.com | WE have things for Mum as well.<br>24 Wattle Lane | Fairview Vic 3999 | Call: 03 5550 1274</p>
  <p class="abs find-us find-us--back">FIND US A WWW.LUMORA-WEAR.COM</p>
</section>

</body>
</html>
```